Business Card Design for Varnor Facility Services

We are looking for a Business Card Design for the Company "Varnor Facility Services."
Front side:
- Company Logo (small)
- Company Name, address, pohone, website and personal data.
- white background, for text e.g. company colors (blue or green like in the logo)
Please use following data:
Company data:
Varnor Facility Services Kuttelbrand
Lindauweg 14
8904 Felsach
www.varnor-fs.example
Person data:
Tobias Kuttelbrand
Geschäftsführer
+41 76 915 47 18
info@varnor-fs.example
Back side:
could be colored in blue or green
please use a big logo sing and some smaller icons to say what is all beeing offered in facility services, like cleaning, maintenance cleaning
industrial cleaning, caretaking, gardening, disposal. There is no need for everyone of the icons if there are similar or an icon is standing for more of them.
Cleaning Service
colors to use:
blue: HEX 246BB0
green: HEX 52B33E

```html
<!DOCTYPE html>
<html lang="de">
<head>
<meta charset="utf-8">
<title>Varnor Facility Services – Business Card</title>
<link href="https://fonts.googleapis.com/css2?family=Lato:wght@400;700;900&display=swap" rel="stylesheet">
<style>
  :root {
    --brand-blue: #246BB0;
    --brand-green: #52B33E;
    --backdrop: #dcdcde;
    --card-white: #ffffff;
    --ink: #1f1f1f;
  }
  * { margin: 0; padding: 0; box-sizing: border-box; }
  html, body {
    width: 1200px; height: 900px; overflow: hidden;
    background: var(--backdrop);
    font-family: "Lato", sans-serif;
  }
  .stage { position: relative; width: 1200px; height: 900px; }

  .card {
    position: absolute;
    width: 540px; height: 320px;
    border-radius: 26px;
    box-shadow: 0 10px 24px rgba(0,0,0,0.18);
    overflow: hidden;
  }

  /* Back side */
  .card--back {
    left: 130px; top: 110px;
    background: var(--brand-blue);
    color: #fff;
    display: flex; flex-direction: column; align-items: center;
  }
  .service-emblem {
    margin-top: 60px;
    width: 130px; height: 120px;
    border-radius: 14px;
    background: linear-gradient(160deg, #ffffff 0%, #e3ecf6 100%);
    opacity: 0.92;
  }
  .service-list {
    margin-top: 52px;
    text-align: center;
    font-size: 14px;
    letter-spacing: 0.06em;
    line-height: 1.35;
    text-transform: uppercase;
  }

  /* Front side */
  .card--front {
    left: 530px; top: 450px;
    background: var(--card-white);
    color: var(--ink);
  }
  .brand {
    position: absolute; left: 34px; top: 44px;
    display: flex; align-items: center; gap: 12px;
  }
  .brand__dot {
    width: 22px; height: 22px; border-radius: 50%;
    background: var(--brand-green);
  }
  .brand__name {
    font-weight: 900; font-size: 26px;
    color: var(--brand-blue);
    letter-spacing: 0.02em;
  }
  .company-address {
    position: absolute; right: 34px; top: 118px;
    text-align: right; font-size: 16px; line-height: 1.25;
    font-style: normal;
  }
  .company-address .company-name { color: var(--brand-blue); }

  .person {
    position: absolute; left: 34px; bottom: 28px;
  }
  .person__name {
    font-weight: 900; font-size: 21px;
    color: var(--brand-blue);
    text-transform: uppercase; letter-spacing: 0.03em;
  }
  .person__role { font-size: 16px; margin-bottom: 8px; }
  .contact-list { list-style: none; font-size: 16px; line-height: 1.45; }
  .contact-list li { display: flex; align-items: center; gap: 9px; }
  .contact-list svg { width: 14px; height: 14px; flex: none; }
</style>
</head>
<body>
<main class="stage">

  <section class="card card--back" aria-label="Card back side">
    <div class="service-emblem" role="img" aria-label="Broom with soap bubbles cleaning illustration"></div>
    <p class="service-list">
      Cleaning | Maintenance Cleaning | Industrial Cleaning<br>
      Caretaking | Gardening | Disposal
    </p>
  </section>

  <section class="card card--front" aria-label="Card front side">
    <div class="brand">
      <span class="brand__dot"></span>
      <span class="brand__name">Varnor Facility Services</span>
    </div>

    <address class="company-address">
      <span class="company-name">Varnor Facility Services<br>Kuttelbrand</span><br>
      Lindauweg 14<br>
      8904 Felsach
    </address>

    <div class="person">
      <p class="person__name">Tobias Kuttelbrand</p>
      <p class="person__role">Geschäftsführer</p>
      <ul class="contact-list">
        <li>
          <svg viewBox="0 0 16 16" aria-hidden="true"><path fill="#246BB0" d="M3 1.5l3 .5 1 3-2 1.5a9 9 0 0 0 4.5 4.5L11 9l3 1 .5 3-2 1.5C6.5 14 2 9.5 1.5 3.5z"/></svg>
          +41 76 915 47 18
        </li>
        <li>
          <svg viewBox="0 0 16 16" aria-hidden="true"><rect x="1" y="3" width="14" height="10" rx="1" fill="#246BB0"/><path d="M1.5 3.8L8 9l6.5-5.2" stroke="#fff" stroke-width="1.3" fill="none"/></svg>
          info@varnor-fs.example
        </li>
        <li>
          <svg viewBox="0 0 16 16" aria-hidden="true"><circle cx="8" cy="8" r="7" fill="#246BB0"/><path d="M1 8h14M8 1c-3 3.5-3 10.5 0 14M8 1c3 3.5 3 10.5 0 14" stroke="#fff" stroke-width="1" fill="none"/></svg>
          www.varnor-fs.example
        </li>
      </ul>
    </div>
  </section>

</main>
</body>
</html>
```